Kelvar Systems Website

Website design for our company: Kelvar Systems.
The website should look fresh and IT focused. Please have a look at http://www.kelvarsystems.net.au/ for our current design. We want something fresh and new, professional looking, in WordPress so we can easily make changes.

Industry/Entity Type

It Company

```html
<!DOCTYPE html>
<html lang="en">
<head>
<meta charset="utf-8">
<title>Kelvar Systems</title>
<link rel="stylesheet" href="https://fonts.googleapis.com/css2?family=Open+Sans:ital,wdth,wght@0,75..100,300..800;1,75..100,300..800&display=swap">
<style>
  :root {
    --green: #00b259;
    --green-dark: #009a4c;
    --topbar: #2f2f31;
    --heading-grey: #6b7071;
    --text: #3a3a3a;
    --soft-grey: #e8e8ea;
    --band-grey: #dcdcdd;
    --rule: #c8c8c8;
    --white: #ffffff;
  }
  * { box-sizing: border-box; margin: 0; padding: 0; }
  html, body { width: 788px; height: 1200px; overflow: hidden; background: var(--white); }
  body { position: relative; font-family: "Open Sans", Arial, sans-serif; color: var(--text); }
  .abs { position: absolute; }
  .condensed { font-stretch: 75%; font-weight: 700; }

  .top-bar { left: 0; top: 0; width: 788px; height: 25px; background: var(--topbar); color: var(--white);
    font-size: 9.5px; text-align: center; line-height: 25px; }

  .site-header { left: 0; top: 25px; width: 788px; height: 56px; background: var(--green); }
  .brand { left: 46px; top: 10px; display: flex; align-items: center; gap: 10px; color: var(--white);
    font-weight: 700; font-size: 16px; }
  .brand-dot { width: 36px; height: 36px; border-radius: 50%; background: var(--white); }
  .main-nav { right: 48px; top: 0; height: 56px; display: flex; gap: 18px; align-items: center; }
  .main-nav a { color: var(--white); text-decoration: none; font-size: 10.5px; font-weight: 700; }

  .hero { left: 0; top: 81px; width: 788px; height: 287px;
    background: linear-gradient(120deg, #6b6e73 0%, #2d3a52 22%, #8a7a5e 45%, #b89a6e 70%, #c9ae84 100%); }
  .search-box { left: 163px; top: 190px; width: 465px; height: 45px; background: #ececec;
    border: 3px solid #b3b3b3; display: flex; align-items: center; padding: 0 10px; justify-content: space-between; }
  .search-box span { font-size: 16px; font-weight: 700; color: #2a2a2a; }
  .search-scope { left: 164px; top: 241px; display: flex; gap: 28px; color: var(--white); font-size: 9.5px; font-weight: 700; }
  .search-scope label { display: flex; align-items: center; gap: 6px; }
  .radio { width: 14px; height: 14px; border-radius: 50%; background: #ddd; border: 2px solid #999; }
  .radio.on { background: #fff; box-shadow: inset 0 0 0 3px #ddd, inset 0 0 0 6px #666; }

  .welcome-title { left: 46px; top: 388px; font-size: 35px; color: var(--heading-grey); }
  .welcome-rule { left: 46px; top: 434px; width: 398px; height: 1px; background: var(--rule); }
  .welcome-copy { left: 46px; top: 448px; width: 398px; font-size: 12.2px; line-height: 14.2px; }
  .welcome-copy p { margin-bottom: 14px; }

  .director { left: 45px; top: 621px; width: 399px; height: 82px; background: var(--soft-grey); }
  .director-photo { left: 13px; top: 8px; width: 58px; height: 58px; border-radius: 50%;
    background: radial-gradient(circle at 50% 40%, #b48b6c, #5a4536); }
  .director-name { left: 82px; top: 16px; font-size: 11.5px; font-weight: 700; font-style: italic; line-height: 13px; color: #333; }
  .director-quote { left: 79px; top: 48px; font-size: 9.5px; font-style: italic; color: #777; }

  .remote { left: 465px; top: 389px; width: 278px; height: 174px;
    background: linear-gradient(135deg, #2a2a2a, #4d4d4d 55%, #3a3a3a); }
  .remote-title { left: 0; width: 278px; top: 10px; text-align: center; font-size: 27px; color: var(--white); }
  .remote-rule { left: 24px; top: 53px; width: 229px; height: 1px; background: #bbb; }
  .remote-input { left: 21px; top: 69px; width: 235px; height: 34px; background: #e4e4e4; border: 3px solid #8c8c8c;
    font-size: 10px; font-weight: 600; color: #666; padding-left: 9px; line-height: 28px; }
  .remote-button { left: 84px; top: 118px; width: 108px; height: 29px; background: var(--green); color: var(--white);
    font-size: 10.5px; font-weight: 700; text-align: center; line-height: 29px; border-radius: 2px; }

  .services { left: 0; top: 736px; width: 788px; height: 110px; background: var(--green); color: var(--white); }
  .services-title { left: 46px; top: 36px; font-size: 29px; }
  .service-list { font-size: 12px; list-style: none; }
  .service-list li { height: 24.5px; display: flex; align-items: center; gap: 4px; }

  .testimonials { left: 0; top: 846px; width: 788px; height: 325px; background: var(--band-grey); }
  .testimonials-title { left: 46px; top: 19px; font-size: 27px; color: var(--heading-grey); }
  .testimonials-rule { left: 46px; top: 57px; width: 697px; height: 1px; background: #bcbcbc; }
  .quote-card { background: var(--white); border-radius: 5px; padding: 14px 14px; font-size: 12px; line-height: 15.2px; color: #555; }
  .quote-card p + p { margin-top: 15px; }
  .quote-tail { width: 0; height: 0; border-left: 14px solid var(--white); border-bottom: 12px solid transparent; }
  .quote-author { font-size: 9.5px; color: #444; }

  .site-footer { left: 0; top: 1171px; width: 788px; height: 29px; text-align: center; line-height: 29px;
    font-size: 9.5px; color: #777; }
</style>
</head>
<body>
  <div class="abs top-bar">Your IP address is 127.0.0.1 which resolves to xxx.yyy.xxx.255</div>

  <header class="abs site-header">
    <div class="abs brand"><span class="brand-dot"></span><span>Kelvar Systems</span></div>
    <nav class="abs main-nav">
      <a href="#">HOME</a><a href="#">CLIENTS</a><a href="#">SERVICES</a><a href="#">SUPPORT AREAS</a><a href="#">ABOUT US</a><a href="#">CONTACT US</a>
    </nav>
  </header>

  <section class="abs hero" role="img" aria-label="Photo of computer workstations with monitors and keyboards in an office"></section>
  <div class="abs search-box">
    <span>Search...</span>
    <svg width="18" height="18" viewBox="0 0 18 18"><circle cx="7.5" cy="7.5" r="5.5" fill="none" stroke="#2a2a2a" stroke-width="2.4"/><line x1="11.5" y1="11.5" x2="16.5" y2="16.5" stroke="#2a2a2a" stroke-width="2.8" stroke-linecap="round"/></svg>
  </div>
  <div class="abs search-scope">
    <label><span class="radio on"></span>LOCAL</label>
    <label><span class="radio"></span>WEB</label>
  </div>

  <h1 class="abs welcome-title condensed">Welcome to Kelvar Systems</h1>
  <div class="abs welcome-rule"></div>
  <div class="abs welcome-copy">
    <p>Kelvar Systems is an Adelaide based company with a single objective - to excel in the support and service of all computer and IT needs.</p>
    <p>We provide a high level of consulting services using the most experienced engineers at a reasonable and fair price. We believe in using a Business Value approach to every aspect of computer consulting to provide our clients with the most cost effective solutions.</p>
    <p>We strongly believe that we are in business with our clients. Each thing we do must be measured against our clients' business objectives. At the end of the day our client's success is our success.</p>
  </div>

  <div class="abs director">
    <div class="abs director-photo" role="img" aria-label="Portrait photo of the managing director"></div>
    <div class="abs director-name">Daniel Reeves<br>Managing Director</div>
    <div class="abs director-quote">“Lorem ipsum dolor sit amet, consectetur adipiscing elit.”</div>
  </div>

  <aside class="abs remote" role="img" aria-label="Photo of a support technician wearing a headset">
    <h2 class="abs remote-title condensed">Remote Support</h2>
    <div class="abs remote-rule"></div>
    <div class="abs remote-input">Enter your 6-digit code</div>
    <div class="abs remote-button">CONNECT NOW</div>
  </aside>

  <section class="abs services">
    <h2 class="abs services-title condensed">Our Services:</h2>
    <ul class="abs service-list" style="left:225px;top:18px">
      <li><svg width="10" height="9" viewBox="0 0 10 9"><path d="M1 5l3 3 5-7" fill="none" stroke="#fff" stroke-width="2.2"/></svg>On-site Service</li>
      <li><svg width="10" height="9" viewBox="0 0 10 9"><path d="M1 5l3 3 5-7" fill="none" stroke="#fff" stroke-width="2.2"/></svg>Remote Desktop Support</li>
      <li><svg width="10" height="9" viewBox="0 0 10 9"><path d="M1 5l3 3 5-7" fill="none" stroke="#fff" stroke-width="2.2"/></svg>Medical IT Service</li>
    </ul>
    <ul class="abs service-list" style="left:405px;top:18px">
      <li><svg width="10" height="9" viewBox="0 0 10 9"><path d="M1 5l3 3 5-7" fill="none" stroke="#fff" stroke-width="2.2"/></svg>Pharmacy IT Service</li>
      <li><svg width="10" height="9" viewBox="0 0 10 9"><path d="M1 5l3 3 5-7" fill="none" stroke="#fff" stroke-width="2.2"/></svg>Website Design</li>
      <li><svg width="10" height="9" viewBox="0 0 10 9"><path d="M1 5l3 3 5-7" fill="none" stroke="#fff" stroke-width="2.2"/></svg>Disaster Recovery</li>
    </ul>
    <ul class="abs service-list" style="left:585px;top:18px">
      <li><svg width="10" height="9" viewBox="0 0 10 9"><path d="M1 5l3 3 5-7" fill="none" stroke="#fff" stroke-width="2.2"/></svg>Hardware/ Software supply</li>
      <li><svg width="10" height="9" viewBox="0 0 10 9"><path d="M1 5l3 3 5-7" fill="none" stroke="#fff" stroke-width="2.2"/></svg>Consumables</li>
    </ul>
  </section>

  <section class="abs testimonials">
    <h2 class="abs testimonials-title condensed">What do our clients say about Kelvar?</h2>
    <div class="abs testimonials-rule"></div>

    <blockquote class="abs quote-card" style="left:45px;top:69px;width:339px;height:215px">
      <p>“I have used Kelvar Systems as a primary supplier of hardware &amp; computer support for the last 5 years, at both the Morven &amp; Hale and the Corbell Pharmacy groups, where I have been employed as an I.T. Coordinator/Support Officer. Dane &amp; his team are always friendly, prompt &amp; conscientious. They have an excellent wealth of knowledge &amp; I.T. savvy, always willing to ‘go the extra mile’ to get the job done.</p>
      <p>Their excellent knowledge of all POS systems is nice to know, to get you out of all sorts of problem situations. Not only that, someone is always contactable from Kelvar Systems, no matter what time of the day.”</p>
    </blockquote>
    <div class="abs quote-tail" style="left:70px;top:284px"></div>
    <div class="abs quote-author" style="left:93px;top:290px">Michael Ostrander B.Pharm AACPA Parkline Chemists, Angle Vale</div>

    <blockquote class="abs quote-card" style="left:405px;top:69px;width:339px;height:108px">
      <p>“I have always found the team extremely helpful with their advice over the phone. They also have the ability to access our computers remotely, and can rectify most problems quite swiftly. I have no hesitation in recommending Kelvar Systems for all of your IT needs.”</p>
    </blockquote>
    <div class="abs quote-tail" style="left:431px;top:177px"></div>
    <div class="abs quote-author" style="left:457px;top:185px">Jeff Calloway (Morven &amp; Hale Pharmacy Group)</div>
  </section>

  <footer class="abs site-footer">Copyright © 2013 Kelvar Systems Pty Ltd. All Rights Reserved.</footer>
</body>
</html>
```